Business card for my company-RMK Design Studio

I do not have a logo-I like red and keeping it clean. Information that should be on the card:
Tom Brakefield AIA
Architecture Planning Interiors
Cell Phone-614.492.5068
email-rmkarchitect1@lunvale.com
www.rmkdesignstudio.net

```html
<!DOCTYPE html>
<html lang="en">
<head>
<meta charset="utf-8">
<title>RMK Design Studio — Business Card</title>
<link rel="stylesheet" href="https://fonts.googleapis.com/css2?family=Bodoni+Moda:wght@500&family=Montserrat:wght@400&display=swap">
<style>
  :root {
    --backdrop: #e2e2e2;
    --card: #f7f7f7;
    --card-tone: #f1f1f1;
    --ink: #151515;
    --mark: #c0262d;
    --shadow: rgba(0, 0, 0, 0.18);
  }
  * { margin: 0; padding: 0; box-sizing: border-box; }
  html, body {
    width: 987px;
    height: 1200px;
    overflow: hidden;
    background: var(--backdrop);
  }
  .sheet { position: relative; width: 987px; height: 1200px; }
  .card {
    position: absolute;
    left: 74px;
    width: 838px;
    height: 523px;
    background: var(--card);
    box-shadow: 0 1px 3px var(--shadow);
    overflow: hidden;
  }
  .card--front { top: 59px; }
  .card--back { top: 620px; }
  .card__texture {
    position: absolute;
    inset: 0;
    background: linear-gradient(180deg, var(--card) 0%, var(--card-tone) 50%, var(--card) 100%);
  }
  .brand-square {
    position: absolute;
    background: var(--mark);
  }
  .serif {
    position: absolute;
    font-family: "Bodoni Moda", "Didot", serif;
    font-weight: 500;
    color: var(--ink);
    line-height: 1;
    white-space: nowrap;
  }
  .card--front .brand-square { left: 339px; top: 82px; width: 146px; height: 146px; }
  .card--front .studio-name { left: 0; width: 838px; text-align: center; top: 300px; font-size: 68px; }
  .card--front .disciplines { left: 0; width: 838px; text-align: center; top: 382px; font-size: 38px; }

  .card--back .brand-square { left: 171px; top: 98px; width: 90px; height: 90px; }
  .card--back .studio-name { left: 44px; top: 221px; font-size: 38px; }
  .card--back .disciplines { left: 45px; top: 268px; font-size: 22px; }
  .card--back .person-name { left: 40px; top: 364px; font-size: 38px; }

  .contact-list { list-style: none; }
  .contact {
    position: absolute;
    left: 449px;
    display: flex;
    align-items: center;
    gap: 14px;
    font-family: "Montserrat", "Helvetica Neue", Arial, sans-serif;
    font-size: 22px;
    color: var(--ink);
    white-space: nowrap;
  }
  .contact--phone { top: 358px; }
  .contact--email { top: 404px; }
  .contact--web { top: 456px; }
  .contact__icon { width: 34px; height: 34px; flex: none; }
  .contact__text { position: relative; top: -6px; }
</style>
</head>
<body>
<main class="sheet">
  <section class="card card--front">
    <div class="card__texture" role="img" aria-label="Faint pale grey diamond pattern across the card"></div>
    <div class="brand-square" aria-hidden="true"></div>
    <h1 class="serif studio-name">RMK Design Studio</h1>
    <p class="serif disciplines">Architecture Planning Interiors</p>
  </section>

  <section class="card card--back">
    <div class="card__texture" role="img" aria-label="Faint pale grey diamond pattern across the card"></div>
    <div class="brand-square" aria-hidden="true"></div>
    <h2 class="serif studio-name">RMK Design Studio</h2>
    <p class="serif disciplines">Architecture Planning Interiors</p>
    <p class="serif person-name">Tom Brakefield AIA</p>
    <ul class="contact-list">
      <li class="contact contact--phone">
        <svg class="contact__icon" viewBox="0 0 34 34" aria-hidden="true">
          <circle cx="17" cy="17" r="15" fill="none" stroke="var(--ink)" stroke-width="2"/>
          <path d="M12 10.5c1-.8 2-.6 2.5.3l1.2 2.3c.4.8.2 1.4-.5 1.9l-.8.6c.8 1.8 2 3 3.8 3.8l.6-.8c.5-.7 1.1-.9 1.9-.5l2.3 1.2c.9.5 1.1 1.5.3 2.5-1 1.2-2.5 1.6-4 .9-3.6-1.6-6.2-4.2-7.8-7.8-.7-1.5-.3-3 .5-4.4z" fill="var(--ink)"/>
        </svg>
        <span class="contact__text">614.492.5068</span>
      </li>
      <li class="contact contact--email">
        <svg class="contact__icon" viewBox="0 0 34 34" aria-hidden="true">
          <circle cx="17" cy="17" r="15" fill="none" stroke="var(--ink)" stroke-width="2"/>
          <rect x="10" y="12.5" width="14" height="9.5" rx="1" fill="var(--ink)"/>
          <path d="M10.5 13l6.5 5 6.5-5" fill="none" stroke="var(--card)" stroke-width="1.2"/>
        </svg>
        <span class="contact__text">rmkarchitect1@lunvale.com</span>
      </li>
      <li class="contact contact--web">
        <svg class="contact__icon" viewBox="0 0 34 34" aria-hidden="true">
          <circle cx="17" cy="17" r="15" fill="none" stroke="var(--ink)" stroke-width="2"/>
          <path d="M13 10l9 6.5-4 .8 2.3 4.8-1.8.9-2.3-4.8-3.2 2.6z" fill="var(--ink)"/>
        </svg>
        <span class="contact__text">www.rmkdesignstudio.net</span>
      </li>
    </ul>
  </section>
</main>
</body>
</html>
```